Movie Genre Illustrations

We need a dozen of illustrations for movie genres for an online video store.

The dimensions for the images is 650 x 240.
The images will be placed on a dark background.

The images should be a mixture of some unique font displaying the 'attitude' of the genre, with complementing background image.

An example for "Kids"
a colourful balloon background with a childish font.
An example for "Science Fiction"
a starscape background with some futuristic font.

The categories are as below, the text in quotes is the danish text and should be the text shown in the illustrations, the preceding translations are added for your convenience:

Action "Action"
Comedy "Komedie"
Science Fiction "Science Fiction"
Thriller "Thriller"
Drama "Drama"
Romance "Romantik"
Animation "Animation"
Kids "Børnefilm"
Danish Movies "Danske film" // if you don't know much about Denmark you can skip this one.
War Movies "Krigsfilm"
Horror "Gyser"
Adventure "Eventyr"
Crime "Krimi"
Stand-up "Stand-up og satire"
Youth "Ungdom"
Documentary "Dokumentar"
Martial Arts (kung fu movies) "Kampsport"

For inspiration look to some of the feature banners in the Plexio store promoting genre specific content (more examples in the App section of the Plexio store).

important, these images will be presented on a TV, please avoid using large white areas, and make sure the white you use is #f1f1f1 instead of #fff.

There are two designs right now, both of them are way too noisy, there are way too many elements, and the backgrounds are crowded, please simplify things, this is for a scandinavian audience, simplicity is key (think olbu).

Danish TV users

Movie

```html
<!DOCTYPE html>
<html lang="da">
<head>
<meta charset="utf-8">
<title>Genre banners</title>
<link href="https://fonts.googleapis.com/css2?family=Righteous&family=Jost:wght@700&family=Chewy&display=swap" rel="stylesheet">
<style>
  :root {
    --board: #f1f1f1;
    --frame: #1b1b1b;
    --sky-deep: #1a6f8c;
    --sky-light: #2ad0ec;
    --gold-light: #ffe94a;
    --gold-deep: #f0a800;
    --gold-edge: #b87400;
    --night: #0c0d0c;
    --stone: #5d6358;
    --silver-light: #ffffff;
    --silver-deep: #9a9a9a;
    --meadow-deep: #1f5a1a;
    --meadow-light: #9ad43a;
    --sun-yellow: #fff21a;
    --sun-orange: #f08a00;
  }
  * { margin: 0; padding: 0; box-sizing: border-box; }
  html, body { width: 1200px; height: 900px; overflow: hidden; }
  body {
    background: var(--frame);
    position: relative;
  }
  .board {
    position: absolute;
    left: 12px; top: 12px;
    width: 1176px; height: 876px;
    background: var(--board);
    box-shadow: inset 0 0 40px rgba(0,0,0,0.35);
  }
  .banner {
    position: absolute;
    left: 275px;
    width: 650px;
    height: 240px;
    overflow: hidden;
    display: flex;
    align-items: center;
    justify-content: center;
  }
  .banner__art { position: absolute; inset: 0; }
  .banner__title { position: relative; line-height: 1; }

  .banner--animation { top: 76px; }
  .banner--animation .banner__art {
    background:
      radial-gradient(ellipse at 85% 0%, rgba(255,255,255,0.35), transparent 50%),
      linear-gradient(100deg, var(--sky-deep), #1f9cbc 55%, var(--sky-light));
  }
  .banner--animation .banner__title {
    font-family: "Righteous", sans-serif;
    font-size: 108px;
    letter-spacing: -2px;
    background: linear-gradient(180deg, var(--gold-light) 20%, var(--gold-deep) 85%);
    -webkit-background-clip: text;
    background-clip: text;
    color: transparent;
    filter: drop-shadow(0 3px 0 var(--gold-edge)) drop-shadow(6px 8px 6px rgba(0,30,50,0.55));
    margin-top: 10px;
  }

  .banner--krimi { top: 331px; }
  .banner--krimi .banner__art {
    background:
      radial-gradient(ellipse at 55% 20%, #78806f, transparent 60%),
      linear-gradient(160deg, var(--night) 10%, var(--stone) 50%, #2d302b 80%, var(--night));
  }
  .banner--krimi .banner__title {
    font-family: "Jost", sans-serif;
    font-weight: 700;
    font-size: 116px;
    letter-spacing: 10px;
    background: linear-gradient(180deg, var(--silver-light) 25%, var(--silver-deep));
    -webkit-background-clip: text;
    background-clip: text;
    color: transparent;
    filter: drop-shadow(0 3px 1px rgba(0,0,0,0.8));
    margin-left: 10px;
  }

  .banner--kids { top: 584px; }
  .banner--kids .banner__art {
    background:
      radial-gradient(circle at 93% 15%, rgba(240,210,90,0.7), transparent 18%),
      radial-gradient(circle at 4% 75%, rgba(230,150,60,0.6), transparent 16%),
      radial-gradient(ellipse at 50% 35%, var(--meadow-light), #46951f 55%, var(--meadow-deep));
  }
  .banner--kids .banner__title {
    font-family: "Chewy", cursive;
    font-size: 118px;
    background: linear-gradient(180deg, var(--sun-orange) 10%, var(--sun-yellow) 50%, var(--sun-orange) 95%);
    -webkit-background-clip: text;
    background-clip: text;
    color: transparent;
    filter: drop-shadow(6px 8px 2px rgba(20,40,0,0.75));
    margin-top: 14px;
  }
</style>
</head>
<body>
  <main class="board">
  </main>

  <section class="banner banner--animation">
    <div class="banner__art" role="img" aria-label="Blue sky with soft clouds and sun rays"></div>
    <h2 class="banner__title">ANIMATION</h2>
  </section>

  <section class="banner banner--krimi">
    <div class="banner__art" role="img" aria-label="Dark pavement with long shadows of a fence"></div>
    <h2 class="banner__title">KRIMI</h2>
  </section>

  <section class="banner banner--kids">
    <div class="banner__art" role="img" aria-label="Green sunburst with colourful balloons"></div>
    <h2 class="banner__title">Børnefilm</h2>
  </section>
</body>
</html>
```